Velmo for Dental office

We are a dental office that are planning to add velmo to our treatment and we are in need of nice flyer to catch eyes.
attached is our logo and also a file that gives you a few items that are nice to place in the flyer- we are looking for two sizes, one postal card sized and one letter size. You can pick and choose from the document sent here in your design. Also find some royalty free images to be added to the flyer . Let me know if you need anything else.
PLEASE NOTE. The design needs to be more graphic and less in writing, the document attached is for you to choose what catches eyes and use it in flyer. You can add some details, bullet points , things that matter to customer but don't make the flyer too noisy, busy. The flyer color needs to be harmonious and match website colors

```html
<!DOCTYPE html>
<html lang="en">
<head>
<meta charset="utf-8">
<title>Tall Pines Dental – Velmo Postcard</title>
<link href="https://fonts.googleapis.com/css2?family=Fira+Sans:wght@300;400;500;600;700&family=Rubik:wght@800&display=swap" rel="stylesheet">
<style>
  :root{
    --teal:#1b6f73;
    --sky:#5bbfcf;
    --brown:#8a4f1f;
    --yellow:#f7c84a;
    --orange:#f08a3a;
    --cream:#fdeaa6;
    --ink:#1f1f1f;
    --backdrop:#7b7b7b;
    --rule:#c9c9c9;
  }
  *{box-sizing:border-box;margin:0;padding:0}
  html,body{width:1200px;height:904px;overflow:hidden}
  body{background:var(--backdrop);font-family:"Fira Sans",sans-serif;color:var(--ink)}
  .canvas{position:relative;width:1200px;height:904px;overflow:hidden;background:var(--backdrop)}

  .postcard{position:absolute;width:487px;height:347px;background:#fff;overflow:hidden}
  .postcard--front{left:211px;top:75px}
  .postcard--back{left:502px;top:481px}
  .postcard__art{position:absolute;inset:0;width:100%;height:100%}

  .brand{position:absolute;display:flex;align-items:center;gap:8px}
  .brand__dot{border-radius:50%;background:var(--orange);flex:none}
  .brand__name{font-family:"Fira Sans",sans-serif;font-weight:600;color:var(--teal);line-height:1}
  .postcard--front .brand{left:18px;top:22px}
  .postcard--front .brand__dot{width:40px;height:40px}
  .postcard--front .brand__name{font-size:19px}
  .postcard--back .brand{left:293px;top:20px;gap:6px}
  .postcard--back .brand__dot{width:22px;height:22px}
  .postcard--back .brand__name{font-size:10.5px}

  .headline-band{position:absolute;left:0;top:90px;width:240px;height:69px;background:var(--brown);padding:10px 0 0 17px}
  .headline{font-family:"Rubik",sans-serif;font-weight:800;color:var(--yellow);font-size:13px;line-height:16.3px}

  .benefits{position:absolute;left:17px;top:166px;width:240px}
  .section-title{font-weight:700;color:var(--teal);font-size:11px;line-height:13px}
  .section-title small{font-size:7.5px;font-weight:600}
  sup{font-size:.5em;vertical-align:super;line-height:0}

  .ticks{list-style:none;font-size:8.6px;font-weight:500;line-height:11.2px}
  .ticks li{position:relative;padding-left:11px;margin-top:3.3px}
  .ticks li::before{content:"✓";position:absolute;left:0;top:2.5px;width:6px;height:6px;border-radius:50%;background:var(--teal);color:#fff;font-size:4.5px;line-height:6px;text-align:center;font-weight:700}

  .contact-bar{position:absolute;left:0;bottom:0;width:100%;height:50px;color:#fff;font-size:9.5px;font-weight:500}
  .contact{position:absolute;display:flex;align-items:flex-start;gap:6px;line-height:12.5px}
  .contact svg{width:13px;height:13px;flex:none}
  .contact strong{font-weight:600}
  .contact--address{left:19px;top:12px}
  .contact--phone{left:138px;top:20px}
  .contact--web{left:243px;top:21px}

  .about{position:absolute;left:17px;top:16px;width:238px}
  .about p{font-size:8.6px;font-weight:300;line-height:11.6px;text-align:justify;margin-top:1px}
  .why{position:absolute;left:17px;top:114px;width:250px}
  .why .ticks{font-size:8.6px;line-height:11.4px}
  .why .ticks li{margin-top:2px}
  .pitch{position:absolute;left:17px;top:233px;width:215px;font-size:8.8px;font-weight:500;line-height:12.2px}
  .pitch p+p{margin-top:1px}
  .pitch em{font-style:normal;font-weight:600;color:var(--teal)}
  .cta{position:absolute;left:17px;top:296px;width:250px;color:var(--yellow);font-size:8.7px;line-height:11.6px;font-weight:500}
  .cta__title{font-size:11px;font-weight:700;line-height:14px;margin-bottom:2px}
  .cta strong{color:#fff;font-weight:600}
  .cta span{color:var(--yellow)}

  .return-address{position:absolute;left:332px;top:50px;font-size:8px;line-height:10px;color:var(--ink)}
  .stamp-box{position:absolute;left:421px;top:18px;width:47px;height:47px;border:1.5px solid var(--rule)}
  .address-line{position:absolute;right:19px;height:1px;background:var(--rule)}
</style>
</head>
<body>
<div class="canvas">

  <!-- Front -->
  <section class="postcard postcard--front">
    <svg class="postcard__art" viewBox="0 0 487 347" aria-hidden="false">
      <defs>
        <linearGradient id="coupleTones" x1="0" y1="0" x2="1" y2="1">
          <stop offset="0" stop-color="#cfd8d2"/>
          <stop offset=".45" stop-color="#e9d8bd"/>
          <stop offset="1" stop-color="#c9b08e"/>
        </linearGradient>
        <linearGradient id="chairsideTones" x1="0" y1="0" x2="1" y2="1">
          <stop offset="0" stop-color="#6b4a36"/>
          <stop offset=".6" stop-color="#a7b7bf"/>
          <stop offset="1" stop-color="#4d4b4d"/>
        </linearGradient>
      </defs>
      <path role="img" aria-label="Photo of a smiling senior couple embracing outdoors" fill="url(#coupleTones)"
            d="M345 0 L487 0 L487 270 C445 285 395 292 352 287 C300 272 256 215 256 150 C256 85 292 30 345 0 Z"/>
      <path d="M337 0 C280 30 244 92 244 160 C244 210 262 243 290 268" fill="none" stroke="var(--sky)" stroke-width="5"/>
      <path d="M258 178 C262 220 278 250 300 272" fill="none" stroke="var(--orange)" stroke-width="3"/>
      <path d="M0 281 C110 316 300 312 487 300 L487 347 L0 347 Z" fill="var(--brown)"/>
      <path d="M0 268 C110 296 250 292 335 280" fill="none" stroke="var(--sky)" stroke-width="3"/>
      <path d="M0 277 C120 301 260 297 345 287" fill="none" stroke="var(--orange)" stroke-width="3"/>
      <path d="M322 313 C400 314 452 298 487 272" fill="none" stroke="var(--orange)" stroke-width="9"/>
      <path d="M330 322 C405 322 455 308 487 288" fill="none" stroke="#fff" stroke-width="3"/>
      <circle cx="299" cy="256" r="60" fill="#fff"/>
      <circle role="img" aria-label="Photo of a dentist greeting a patient in the treatment chair" cx="299" cy="256" r="56" fill="url(#chairsideTones)" stroke="var(--sky)" stroke-width="3"/>
    </svg>

    <div class="brand">
      <span class="brand__dot"></span>
      <span class="brand__name">Tall Pines Dental</span>
    </div>

    <div class="headline-band">
      <h1 class="headline">Enhance Your Smile,<br>Refresh Your Look with<br>Velmo® Cosmetic Treatments!</h1>
    </div>

    <div class="benefits">
      <h2 class="section-title">Benefits of Velmo<sup>®</sup> at <small>[Your Dental Office Name]:</small></h2>
      <ul class="ticks">
        <li>Smooth away wrinkles around the eyes, forehead and mouth</li>
        <li>Non-invasive with no downtime</li>
        <li>Safe &amp; performed by skilled dental professionals</li>
        <li>Results that last 3-6 months</li>
        <li>Enhance your overall facial harmony and confidence</li>
      </ul>
    </div>

    <div class="contact-bar">
      <div class="contact contact--address">
        <svg viewBox="0 0 16 16"><circle cx="8" cy="8" r="7.3" fill="none" stroke="var(--yellow)" stroke-width="1.2"/><path d="M8 3.5a2.8 2.8 0 0 0-2.8 2.8C5.2 8.6 8 11.5 8 11.5s2.8-2.9 2.8-5.2A2.8 2.8 0 0 0 8 3.5z" fill="var(--yellow)"/><circle cx="8" cy="6.3" r="1" fill="var(--brown)"/></svg>
        <div><strong>Tall Pine Dental</strong><br>412 W Harlow Ave</div>
      </div>
      <div class="contact contact--phone">
        <svg viewBox="0 0 16 16"><circle cx="8" cy="8" r="7.3" fill="var(--yellow)"/><path d="M5.4 4.3l1.5-.3.9 2-1 .8a5.5 5.5 0 0 0 2.4 2.4l.8-1 2 .9-.3 1.5c-3.4.3-6.6-2.9-6.3-6.3z" fill="var(--brown)"/></svg>
        <span>(555)014-2290</span>
      </div>
      <div class="contact contact--web">
        <svg viewBox="0 0 16 16" fill="none" stroke="var(--yellow)" stroke-width="1.1"><circle cx="8" cy="8" r="7"/><ellipse cx="8" cy="8" rx="3" ry="7"/><path d="M1 8h14M2 4.5h12M2 11.5h12"/></svg>
        <span>www.tallpinesdental.com</span>
      </div>
    </div>
  </section>

  <!-- Back -->
  <section class="postcard postcard--back">
    <svg class="postcard__art" viewBox="0 0 487 347">
      <defs>
        <linearGradient id="storefrontTones" x1="0" y1="0" x2="0" y2="1">
          <stop offset="0" stop-color="#e7ded3"/>
          <stop offset=".55" stop-color="#5b5a5c"/>
          <stop offset="1" stop-color="#cfc9c0"/>
        </linearGradient>
      </defs>
      <path d="M0 107 L250 107 C262 140 270 180 283 225 L0 225 Z" fill="var(--cream)"/>
      <path d="M0 292 L268 292 C272 312 272 330 266 347 L0 347 Z" fill="var(--brown)"/>
      <path d="M295 0 C268 27 260 62 264 102 C268 142 280 178 292 212" fill="none" stroke="var(--sky)" stroke-width="3"/>
      <path d="M262 70 C260 120 272 165 287 202" fill="none" stroke="var(--orange)" stroke-width="2.5"/>
      <path d="M264 347 C276 330 282 316 292 300" fill="none" stroke="var(--orange)" stroke-width="4"/>
      <circle cx="279" cy="266" r="62" fill="#fff"/>
      <circle role="img" aria-label="Photo of the dental office storefront" cx="279" cy="266" r="57" fill="url(#storefrontTones)" stroke="var(--sky)" stroke-width="3"/>
    </svg>

    <div class="about">
      <h2 class="section-title">What is Velmo<sup>®</sup> Cosmetic?</h2>
      <p>Velmo<sup>®</sup> is a non-surgical injectable treatment designed to relax facial muscles and reduce the appearance of fine lines and wrinkles. As a dental office with expertise in facial anatomy, we provide safe, effective treatments that target areas like forehead lines, crow’s feet, and frown lines to restore a youthful, refreshed appearance.</p>
    </div>

    <div class="why">
      <h2 class="section-title">Why Choose Us for Velmo<sup>®</sup>?</h2>
      <ul class="ticks">
        <li>Trusted dental experts with advanced knowledge<br>of facial anatomy</li>
        <li>Customized Velmo<sup>®</sup> treatments tailored to your<br>individual needs</li>
        <li>Comfortable, relaxing office environment</li>
        <li>Convenient scheduling and affordable pricing options</li>
        <li>Results that complement your smile</li>
      </ul>
    </div>

    <div class="pitch">
      <p><em>Look and feel your best —</em> because your smile deserves more than just teeth care!</p>
      <p><em>CALL US for Special offers for</em> our existing patients and for new patients!</p>
    </div>

    <div class="cta">
      <p class="cta__title">Ready to Refresh Your Look?</p>
      <p><span>Call</span> <strong>(555)014-2290</strong> <span>or visit</span> <strong>www.tallpinesdental.com</strong><br>to schedule your Velmo<sup>®</sup> consultation today!</p>
    </div>

    <div class="brand">
      <span class="brand__dot"></span>
      <span class="brand__name">Tall Pines Dental</span>
    </div>
    <p class="return-address">Tall Pine Dental<br>412 W Harlow Ave</p>
    <div class="stamp-box"></div>
    <div class="address-line" style="top:116px;left:289px"></div>
    <div class="address-line" style="top:146px;left:294px"></div>
    <div class="address-line" style="top:176px;left:306px"></div>
  </section>

</div>
</body>
</html>
```